Webdesign für Maklerbüro
Zielgruppe
Wir sind ein Maklerbüro aus Nürnberg, das sich auf den Verkauf von Eigentumswohnungen und Häuser spezialisiert hat. Mit der neuen Seite möchten wir vor allem Eigentümer ansprechen und über unsere Arbeitsweise informieren. Der Hauptzweck ist damit die Akquise von neuen Objekten, für die Vermittlung. Die Zielgruppe sind vornehmlich Immobilienbesitzer im Alter 40+ und im gehobenen Preissegment.
Aufgabenstellung
Beim Design bitte an den Vorgaben des Logo (Datei beigefügt) orientieren. Bilder und Texte können durch 'Platzhalter' ersetzt werden.
Grundsätzlich stellt es für uns kein Problem dar, sich an Template-Vorlagen zu orientieren. Wir stellen uns eine Seite mit Pfiff und Ideenreichtum – einfach weg vom Standard – vor. Wir verkaufen Immobilien, aber vom verstaubten Krawattenträger sind wir weit entfernt. Wir sind ein junges Unternehmen, das neue Marketingwege beschreitet. Unsere Webseite muss das ausdrücken. Kein Standard, und damit auch keine Standard-Webseite. Designs, die uns gut gefallen (und in die Richtung es auch gehen kann) haben wir beigefügt.

```html
<!DOCTYPE html>
<html lang="de">
<head>
<meta charset="utf-8">
<title>Hauswerk Franken – Immobilienmakler Nürnberg</title>
<link href="https://fonts.googleapis.com/css2?family=Open+Sans:wght@400;600;700&display=swap" rel="stylesheet">
<style>
:root{
  --navy:#1f2544;
  --blue:#1a97d5;
  --hero:#4b5e95;
  --text:#2a2f45;
  --white:#ffffff;
}
*{box-sizing:border-box;margin:0;padding:0}
html,body{width:1200px;height:4315px;overflow:hidden;background:#fff}
body{position:relative;font-family:"Open Sans",sans-serif;color:var(--text)}
.abs{position:absolute}
.center{text-align:center}

/* header */
.brand{left:100px;top:40px;font-size:27px;font-weight:600;color:var(--navy);letter-spacing:.5px;display:flex;align-items:center;gap:10px}
.brand .mark{width:16px;height:16px;background:var(--navy)}
.contact-top{right:100px;top:28px;font-size:19px;font-weight:600;color:var(--navy);display:flex;gap:26px}
.contact-top svg{vertical-align:-3px;margin-right:6px}
.nav{right:100px;top:66px;display:flex;gap:20px;font-size:14px;color:var(--navy);border-bottom:2px solid var(--navy);padding-bottom:4px;padding-left:28px}
.nav .active{color:var(--blue)}

/* hero */
.hero{left:0;top:115px;width:1200px;height:542px;background:var(--hero);overflow:hidden}
.hero-photo{position:absolute;right:0;top:0;width:700px;height:542px;
  background:
    linear-gradient(90deg,var(--hero) 0%,rgba(75,94,149,0) 30%),
    radial-gradient(ellipse 18% 10% at 62% 45%,rgba(233,190,110,.75) 0%,rgba(233,190,110,0) 100%),
    radial-gradient(ellipse 14% 9% at 93% 70%,rgba(233,190,110,.7) 0%,rgba(233,190,110,0) 100%),
    linear-gradient(180deg,#8c84a6 0%,#6a6b95 18%,#3f4a68 40%,#3a4360 62%,#5b6072 78%,#8e909c 92%,#6f737f 100%)}
.hero-kicker{left:97px;top:226px;color:#fff;font-size:29px;font-weight:400}
.hero-title{left:97px;top:264px;color:#fff;font-size:45px;font-weight:700;line-height:55px;letter-spacing:.5px}
.btn-outline{display:block;border:2px solid currentColor;text-align:center;font-size:19px;line-height:38px}
.hero-btn{left:100px;top:400px;width:223px;color:#fff}

/* intro */
.h2{font-size:33px;font-weight:700;color:var(--navy);width:1200px;left:0}
.sub{font-size:25px;color:var(--navy);width:1200px;left:0}
.intro-text{left:227px;top:826px;width:746px;font-size:12.5px;line-height:18px;text-align:center;color:var(--text)}

/* feature */
.feature{left:100px;top:1014px;width:1000px;height:561px;
  background:
    radial-gradient(ellipse 38% 30% at 38% 42%,rgba(142,120,100,.9) 0%,rgba(142,120,100,0) 100%),
    linear-gradient(180deg,#4aa2ea 0%,#9cc6e8 22%,#8f8a80 40%,#7c7068 58%,#b8b6ac 68%,#7d9a3e 78%,#86a44a 100%)}
.tag{position:absolute;background:var(--blue);color:#fff;font-weight:700;font-size:19px;padding:6px 15px}
.dot{position:absolute;width:22px;height:22px;border-radius:50%;background:var(--blue);border:3px solid #fff}
.sell-panel{left:734px;top:1098px;width:366px;height:394px;background:rgba(26,151,213,.92);color:#fff;padding:30px 33px}
.sell-panel h3{font-size:26px;line-height:32px;font-weight:600;margin-bottom:26px}
.sell-panel p{font-size:12.5px;line-height:18px}
.sell-panel .btn-outline{margin-top:22px;font-size:15px;line-height:28px}

/* services */
.rule{left:475px;width:250px;height:2px;background:var(--blue)}
.service{width:300px;text-align:center}
.service h4{font-size:20px;font-weight:700;color:var(--navy);margin-top:22px}
.service p{font-size:12.5px;line-height:19px;color:var(--text);margin-top:2px}

/* offers */
.offer-photo{position:absolute}
.offer-cap{position:absolute;background:var(--blue);color:#fff;text-align:center}
.offer-cap h5,.offer-head h5{font-size:20px;font-weight:700;margin-top:6px}
.offer-cap p,.offer-head p{font-size:12.5px;line-height:18px}
.offer-head{position:absolute;background:var(--navy);color:#fff;text-align:center}
.more-btn{left:442px;top:2492px;width:314px;color:var(--blue);font-size:19px;line-height:38px}

/* valuation */
.valuation{left:100px;top:2615px;width:1000px;height:563px;
  background:
    radial-gradient(ellipse 8% 14% at 95% 62%,rgba(200,50,55,.85) 0%,rgba(200,50,55,0) 100%),
    radial-gradient(ellipse 20% 14% at 48% 62%,rgba(60,60,66,.7) 0%,rgba(60,60,66,0) 100%),
    linear-gradient(180deg,#f2f1ef 0%,#e6e4df 55%,#cfc8bb 80%,#8c7d66 100%)}
.val-panel{left:100px;top:2615px;width:366px;height:563px;background:rgba(31,37,68,.93);color:#fff;padding:110px 34px 0}
.val-panel h3{font-size:26px;line-height:32px;font-weight:600;margin-bottom:30px}
.val-panel p{font-size:12.5px;line-height:18px}
.val-panel .btn-outline{margin-top:56px;font-size:15px;line-height:30px;width:300px}

/* testimonials */
.quotes{left:0;top:3314px;width:1200px;height:398px;background:var(--blue)}
.avatar{left:500px;top:3337px;width:200px;height:200px;border-radius:50%;background:radial-gradient(circle at 50% 42%,#d8c2b2 0%,#a08674 45%,#4a3a34 80%,#2e2a2a 100%)}
.arrow-btn{top:3473px;width:67px;height:78px;background:var(--navy);display:flex;align-items:center;justify-content:center}
.q-name{left:0;top:3570px;width:1200px;font-size:20px;font-weight:700;color:var(--navy)}
.q-text{left:175px;top:3606px;width:850px;font-size:20px;line-height:26px;color:var(--navy)}

/* footer */
.footer-line{left:0;top:3794px;width:1200px;height:4px;background:var(--navy)}
.foot-brand{left:100px;top:3820px;font-size:27px;font-weight:600;color:var(--navy);letter-spacing:.5px}
.map{left:100px;top:3870px;width:291px;height:292px;
  background:
    radial-gradient(ellipse 30% 20% at 30% 40%,rgba(190,225,180,.9) 0%,rgba(190,225,180,0) 100%),
    radial-gradient(ellipse 25% 18% at 75% 20%,rgba(170,215,235,.8) 0%,rgba(170,215,235,0) 100%),
    linear-gradient(135deg,#ecece6 0%,#e2e6dc 50%,#ebe8df 100%);border:1px solid #ccc}
.address{left:416px;top:3872px;font-size:13px;line-height:18px;color:var(--navy)}
.address a{color:var(--blue);text-decoration:none}
.field{position:absolute;left:670px;width:430px;border:2px solid var(--blue);font-size:11px;font-weight:700;color:var(--blue);padding:7px 8px}
.submit{left:892px;top:4183px;width:208px;color:var(--blue);font-size:15px;line-height:28px}
.bottom-bar{left:0;top:4250px;width:1200px;height:65px;background:var(--navy);color:#fff;font-size:12px;font-weight:700;display:flex;align-items:center;justify-content:center;gap:14px}
</style>
</head>
<body>

<!-- header -->
<div class="abs brand"><span class="mark"></span>HAUSWERK FRANKEN</div>
<div class="abs contact-top">
  <span><svg width="16" height="16" viewBox="0 0 24 24" fill="none" stroke="#1a97d5" stroke-width="2"><path d="M5 3h4l2 5-3 2a11 11 0 0 0 6 6l2-3 5 2v4a2 2 0 0 1-2 2A17 17 0 0 1 3 5a2 2 0 0 1 2-2z"/></svg>0911 4820 3715</span>
  <span><svg width="18" height="14" viewBox="0 0 24 18" fill="none" stroke="#1a97d5" stroke-width="2"><rect x="1" y="1" width="22" height="16"/><path d="M1 1l11 9 11-9"/></svg>info@hauswerk-franken.de</span>
</div>
<nav class="abs nav">
  <span class="active">ÜBER UNS</span><span>VERKÄUFER/VERMIETER</span><span>KÄUFER/MIETER</span><span>BAUTRÄGER</span><span>SERVICE</span>
</nav>

<!-- hero -->
<section class="abs hero">
  <div class="hero-photo" role="img" aria-label="Foto: Einfamilienhaus mit Garagen und beleuchteten Fenstern in der Abenddämmerung"></div>
</section>
<div class="abs hero-kicker">IHR IMMOBILIENMAKLER FÜR DIE</div>
<div class="abs hero-title">METROPOLREGION<br>NÜRNBERG</div>
<a class="abs btn-outline hero-btn">ANGEBOTE ANSEHEN</a>

<!-- intro -->
<h2 class="abs h2 center" style="top:698px">DIE RICHTIGE WAHL DES IMMOBILIENMAKLERS</h2>
<p class="abs sub center" style="top:736px">Lorem ipsum dolor sit amet consetetur</p>
<p class="abs intro-text">Herzlich Willkommen bei der Lukas Brennholt Immobilienberatung in Nürnberg! Sie suchen den passenden Partner rund um das umfassende Thema Immobilien? Dann sind Sie hier genau richtig: egal ob Suche, Verkauf oder Vermietung einer Eigentumswohnung oder eines Hauses. Bei einem so komplexen Thema mit hohen Emotionen, Sachwerten und Auswirkungen auf Ihr tägliches Leben geht es um Vertrauen und ein gutes Gefühl. Sie sollen eine überzeugende Dienstleistung von Ihrem Makler erhalten. Eine umfassende und professionelle Beratung ist dabei für Ihre Zufriedenheit entscheidend. Davon können Sie sich als Eigentümer schon beim ersten gemeinsamen Schritt überzeugen: der transparenten Einwertung Ihrer Immobilie.</p>

<!-- feature -->
<section class="abs feature" role="img" aria-label="Foto: Klinkerhaus mit Rasen und Einfahrt unter blauem Himmel">
  <span class="tag" style="left:33px;top:104px">Vermessung und Fotografie Ihrer Immobilie</span>
  <span class="dot" style="left:109px;top:160px"></span>
  <span class="tag" style="left:320px;top:215px">Hochwertiges Exposé</span>
  <span class="dot" style="left:282px;top:224px"></span>
  <span class="tag" style="left:320px;top:323px">Immobilien-Präsentation</span>
  <span class="dot" style="left:282px;top:332px"></span>
  <span class="tag" style="left:60px;top:416px">Detaillierte Einwertung</span>
  <span class="dot" style="left:127px;top:380px"></span>
</section>
<div class="abs sell-panel">
  <h3>SIE WOLLEN IHR HAUS ODER IHRE WOHNUNG VERKAUFEN?</h3>
  <p>Lorem ipsum dolor sit amet, consetetur sadipscing elitr, sed diam nonumy eirmod tempor invidunt ut labore et dolore magna aliquyam erat, sed diam voluptua. At vero eos et accusam et justo duo dolores et ea rebum. Stet clita kasd gubergren, no sea takimata sanctus est Lorem ipsum dolor sit amet. Lorem ipsum dolor sit amet, consetetur sadipscing elitr, sed diam nonumy eirmod tempor.</p>
  <a class="btn-outline">IMMOBILIE ANBIETEN</a>
</div>

<!-- services -->
<h2 class="abs h2 center" style="top:1614px;font-size:28px">UNSERE LEISTUNGEN IM ÜBERBLICK</h2>
<p class="abs sub center" style="top:1650px">Duis autem vel eum iriure</p>
<div class="abs rule" style="top:1704px"></div>

<div class="abs service" style="left:93px;top:1748px">
  <svg width="100" height="96" viewBox="0 0 100 96" fill="none" stroke="#1a97d5" stroke-width="3" stroke-linejoin="round"><path d="M6 48L50 6l44 42"/><path d="M16 40v52h68V40"/><path d="M70 14v14"/><path d="M34 62l12 12 22-24"/></svg>
  <h4>OBJEKTAUFNAHME</h4>
  <p>Ut wisi enim ad minim veniam, quis nostrud<br>exerci tation ullamcorper suscipit</p>
</div>
<div class="abs service" style="left:440px;top:1748px">
  <svg width="100" height="96" viewBox="0 0 100 96" fill="none" stroke="#1a97d5" stroke-width="3" stroke-linejoin="round"><path d="M28 34L50 12l22 22"/><path d="M34 30v22h32V30"/><path d="M46 52V42h8v10"/><path d="M8 70h18l14 6h16c4 0 4 6 0 6H40"/><path d="M56 80l26-12c6-2 8 4 3 7L58 90H30L8 84"/></svg>
  <h4>VERMARKTUNG</h4>
  <p>Nam liber tempor cum soluta nobis eleifend<br>option congue nihil</p>
</div>
<div class="abs service" style="left:772px;top:1748px">
  <svg width="100" height="96" viewBox="0 0 100 96" fill="none" stroke="#1a97d5" stroke-width="3" stroke-linejoin="round"><path d="M36 22l18-18 14 14-18 18z"/><path d="M48 30l36 36-6 6-36-36"/><path d="M22 82h44M16 92h56"/><path d="M30 82v-8h28v8"/></svg>
  <h4>VERTRAGSABSCHLUSS</h4>
  <p>Duis autem vel eum iriure dolor in hendrerit<br>in vulputate velit esse molestie</p>
</div>

<!-- offers -->
<h2 class="abs h2 center" style="top:1993px;font-size:28px">AKTUELLE ANGEBOTE</h2>

<div class="offer-photo" style="left:0;top:2056px;width:359px;height:317px;background:radial-gradient(ellipse 40% 22% at 40% 68%,rgba(58,74,100,.9) 0%,rgba(58,74,100,0) 100%),linear-gradient(180deg,#efe6d8 0%,#d9c6aa 35%,#a8885f 65%,#6d543e 100%)" role="img" aria-label="Foto: Wohnzimmer mit Sofa und hohen Fenstern"></div>
<div class="offer-cap" style="left:0;top:2373px;width:359px;height:84px">
  <h5>MARIENVORSTADT</h5>
  <p>At vero eos et accusam et justo duo dolores<br>et ea rebum Stet clita kasd gubergren</p>
</div>

<div class="offer-photo" style="left:359px;top:2139px;width:477px;height:318px;background:radial-gradient(ellipse 30% 18% at 50% 55%,rgba(70,66,64,.85) 0%,rgba(70,66,64,0) 100%),linear-gradient(180deg,#f7f7f5 0%,#e8e9e7 45%,#cfcbc3 75%,#e2ded4 100%)" role="img" aria-label="Foto: Helles offenes Wohnzimmer mit Küche"></div>
<div class="offer-head" style="left:359px;top:2056px;width:477px;height:83px">
  <h5>RÖTHENBACH OST</h5>
  <p>Consetetur sadipscing elitr sed diam nonumy eirmod<br>invidunt ut labore et dolore magna tempor</p>
</div>

<div class="offer-photo" style="left:836px;top:2056px;width:364px;height:317px;background:radial-gradient(ellipse 35% 14% at 50% 52%,rgba(230,190,140,.8) 0%,rgba(230,190,140,0) 100%),linear-gradient(180deg,#c9a47a 0%,#9a6b42 35%,#6e4a2e 65%,#8f7a66 100%)" role="img" aria-label="Foto: Küche mit Holzschränken und Theke"></div>
<div class="offer-cap" style="left:836px;top:2373px;width:364px;height:84px">
  <h5>SANDBERG</h5>
  <p>Lorem ipsum dolor sit amet consetetur sadipscing<br>elitr sed diam nonumy eirmod</p>
</div>

<a class="abs btn-outline more-btn">WEITERE ANGEBOTE ANSEHEN</a>

<!-- valuation -->
<section class="abs valuation" role="img" aria-label="Foto: Hand mit Stift über Unterlagen, Taschenrechner und Hausmodell"></section>
<div class="abs val-panel">
  <h3>IMMOBILIEN-<br>BEWERTUNG</h3>
  <p>Lorem ipsum dolor sit amet, consetetur sadipscing elitr, sed diam nonumy eirmod tempor invidunt ut labore et dolore magna aliquyam erat, sed diam voluptua. At vero eos et accusam et justo duo dolores et ea rebum. Stet clita kasd gubergren, no sea takimata sanctus est Lorem ipsum dolor sit amet. Lorem ipsum dolor sit amet, consetetur sadipscing elitr, sed diam nonumy eirmod tempor.</p>
  <a class="btn-outline">MEHR ZUR IMMOBILIENBEWERTUNG</a>
</div>

<!-- testimonials -->
<h2 class="abs h2 center" style="top:3250px;font-size:28px">KUNDENSTIMMEN</h2>
<section class="abs quotes"></section>
<div class="abs avatar" role="img" aria-label="Porträtfoto der Kundin"></div>
<div class="abs arrow-btn" style="left:0"><svg width="40" height="34" viewBox="0 0 40 34" fill="none" stroke="#1a97d5" stroke-width="6"><path d="M38 17H6M18 3L4 17l14 14"/></svg></div>
<div class="abs arrow-btn" style="left:1133px"><svg width="40" height="34" viewBox="0 0 40 34" fill="none" stroke="#1a97d5" stroke-width="6"><path d="M2 17h32M22 3l14 14-14 14"/></svg></div>
<div class="abs q-name center">KARIN FELDMEIER</div>
<p class="abs q-text center">Duis autem vel eum iriure dolor in hendrerit in vulputate velit esse molestie consequat, vel illum dolore eu feugiat nulla facilisis at vero eros et accumsan et iusto odio dignissim qui blandit praesent.</p>

<!-- footer -->
<div class="abs footer-line"></div>
<div class="abs foot-brand">HAUSWERK FRANKEN</div>
<div class="abs map" role="img" aria-label="Karte: Standort des Büros in Nürnberg"></div>
<div class="abs address">
  Lindenhofstraße 24<br>90482 Nürnberg<br><br>
  Telefon: 0911 4820 3715<br>E-Mail: <a>info@hauswerk-franken.de</a>
</div>
<div class="field" style="top:3871px;height:33px">NAME</div>
<div class="field" style="top:3922px;height:33px">E-MAIL</div>
<div class="field" style="top:3974px;height:33px">BETREFF</div>
<div class="field" style="top:4026px;height:139px">NACHRICHT</div>
<a class="abs btn-outline submit">NACHRICHT ABSENDEN</a>

<footer class="abs bottom-bar"><span>IMPRESSUM</span><span>I</span><span>DATENSCHUTZ</span></footer>

</body>
</html>
```